Business Card Design - ThriveMetric

Looking for creative, modern design, two sided for ThriveMetric that is consistent with color and feel of website www.thrivemetric.net.

Back of card will be used to promote products or have a quote revolving around decisions, change, leadership, innovation, creativity. Back should also have space to promote website, but optional to use the icon. Front of the card will need to use the icon and have standard place for name, job title, phone and email. We are not looking to put a mailing address or fax. Also want space to place a few words/phrase explaining what we do...such as individual growth and organizational development or tools, training, information...in addition, want the linkpage icon small on the front somewhere as we are also on linkpage.

Vector file uploaded of icon.

Target Market(s)

Professional coaching for individual growth and organizational development

Industry/Entity Type

Business

Requirements
Must have
• Icon...see attached.

```html
<!DOCTYPE html>
<html lang="en">
<head>
<meta charset="utf-8">
<title>ThriveMetric Business Card</title>
<link rel="stylesheet" href="https://fonts.googleapis.com/css2?family=Lato:wght@400;700&display=swap">
<style>
  :root {
    --canvas-bg: #e6eaed;
    --card-white: #ffffff;
    --ink: #2b2b2b;
    --rule: #4a4a4a;
    --brand-deep: #1b5fa8;
    --brand-mid: #2a7fd0;
    --brand-light: #6cc0ee;
    --back-deep: #0f4f8f;
    --back-light: #2f82c8;
    --back-name: #b9c9d8;
    --icon-blue: #2a6fb8;
  }
  * { box-sizing: border-box; margin: 0; padding: 0; }
  html, body {
    width: 1200px; height: 960px; overflow: hidden;
    background: var(--canvas-bg);
    font-family: "Lato", sans-serif;
  }
  .canvas {
    width: 1200px; height: 960px;
    display: flex; flex-direction: column; align-items: center; justify-content: center;
    gap: 40px;
  }
  .card {
    width: 700px; height: 400px; position: relative; overflow: hidden;
    box-shadow: 0 6px 18px rgba(0,0,0,0.18);
  }
  /* Front */
  .card-front { background: var(--card-white); color: var(--ink); }
  .tagline-band {
    position: absolute; left: 120px; right: 0; top: 78px; height: 38px;
    background: linear-gradient(90deg, var(--brand-deep), var(--brand-mid) 55%, var(--brand-light));
    color: #fff; font-size: 21px; line-height: 38px; padding-left: 60px;
  }
  .brand-mark {
    position: absolute; left: 32px; top: 30px; width: 140px;
    display: flex; flex-direction: column; align-items: center; gap: 6px;
  }
  .brand-dot {
    width: 112px; height: 112px; border-radius: 50%;
    background: radial-gradient(circle at 40% 35%, #e7edf3, #a9bccd);
    border: 6px solid var(--brand-mid);
  }
  .brand-name { font-size: 17px; font-weight: 700; color: var(--brand-deep); }
  .person {
    position: absolute; left: 32px; top: 218px;
    display: flex; align-items: baseline; gap: 8px;
  }
  .person-name { font-size: 32px; }
  .person-title { font-size: 17px; text-transform: uppercase; }
  .person-title::before { content: "| "; }
  .rule { position: absolute; left: 32px; right: 32px; top: 270px; height: 1.5px; background: var(--rule); }
  .contact {
    position: absolute; top: 292px; list-style: none;
    display: flex; flex-direction: column; gap: 10px;
  }
  .contact-primary { left: 32px; font-size: 19px; top: 300px; }
  .contact-online { left: 420px; font-size: 16px; }
  .contact li { display: flex; align-items: center; gap: 10px; }
  .contact svg { width: 20px; height: 20px; flex: none; }
  .contact .web { font-weight: 700; }
  /* Back */
  .card-back {
    background: linear-gradient(135deg, var(--back-deep), var(--back-light) 60%, var(--back-deep));
    display: flex; align-items: center; justify-content: center; gap: 28px;
  }
  .back-dot {
    width: 120px; height: 120px; border-radius: 50%;
    background: radial-gradient(circle at 40% 35%, #e7edf3, #9fb4c8);
    border: 6px solid var(--brand-light);
  }
  .back-name { font-size: 34px; color: var(--back-name); letter-spacing: 1px; }
</style>
</head>
<body>
<main class="canvas">
  <section class="card card-front" aria-label="Card front">
    <div class="tagline-band">individual growth and organizational development</div>
    <div class="brand-mark">
      <div class="brand-dot"></div>
      <span class="brand-name">ThriveMetric</span>
    </div>
    <div class="person">
      <span class="person-name">Dana Whitfield</span>
      <span class="person-title">Chief Innovator</span>
    </div>
    <div class="rule"></div>
    <ul class="contact contact-primary">
      <li>
        <svg viewBox="0 0 20 20" aria-hidden="true"><rect x="3" y="2" width="14" height="16" rx="2" fill="none" stroke="var(--icon-blue)" stroke-width="2"/><rect x="6" y="5" width="8" height="3" fill="var(--icon-blue)"/><circle cx="7" cy="12" r="1" fill="var(--icon-blue)"/><circle cx="10" cy="12" r="1" fill="var(--icon-blue)"/><circle cx="13" cy="12" r="1" fill="var(--icon-blue)"/><circle cx="7" cy="15" r="1" fill="var(--icon-blue)"/><circle cx="10" cy="15" r="1" fill="var(--icon-blue)"/><circle cx="13" cy="15" r="1" fill="var(--icon-blue)"/></svg>
        1-800-555-0142
      </li>
      <li>
        <svg viewBox="0 0 20 20" aria-hidden="true"><rect x="2" y="4" width="16" height="12" fill="none" stroke="var(--icon-blue)" stroke-width="2"/><path d="M2 4l8 7 8-7M2 16l6-6M18 16l-6-6" fill="none" stroke="var(--icon-blue)" stroke-width="1.5"/></svg>
        contact@thrivemetric.net
      </li>
    </ul>
    <ul class="contact contact-online">
      <li>linkpage /thrivemetric</li>
      <li class="web">
        <svg viewBox="0 0 20 20" aria-hidden="true"><path d="M10 2L1 10h3v8h5v-5h2v5h5v-8h3z" fill="var(--icon-blue)"/></svg>
        www.thrivemetric.net
      </li>
    </ul>
  </section>

  <section class="card card-back" aria-label="Card back">
    <div class="back-dot"></div>
    <span class="back-name">ThriveMetric</span>
  </section>
</main>
</body>
</html>
```